Popup-Fenster Design für Öffnungszeiten
Zielgruppe
Planung und Realisierung von individuellen Kaminen.
Aufgabenstellung
Für unsere Website www.wandelhof-nordau.de benötigen wir ein Popup-Fenster für die Startseite. Da das Geschäft nicht jeden Tag und zu festen Zeit geöffnet hat, soll der Kunde direkt sehen können, wann das Geschäft das nächste Mal geöffnet hat. Das Popup-Fenster soll auffällig, jedoch nicht überladen und aufdringlich sein. Einen eigenen Entwurf (der mir nicht gefällt) habe ich hochgeladen. Vielleicht benötigt dieser nur noch einen Feinschliff!? Es muss nicht reckteckig sein, ich bin auch für runde oder ovale Formen offen. Der dort eingesetzte Text sollte als Platzhalter eingesetzt werden. Bei Fragen können Sie mir gerne eine Nachricht zukommen lassen.

```html
<!DOCTYPE html>
<html lang="de">
<head>
<meta charset="utf-8">
<title>Wandelhof – Popup Öffnungszeiten</title>
<link href="https://fonts.googleapis.com/css2?family=Raleway:wght@200;300;400&family=Roboto:wght@400&family=Playfair+Display:ital,wght@1,700&display=swap" rel="stylesheet">
<style>
  :root {
    --gold: #e3cd7f;
    --gold-deep: #c9b066;
    --ink: #050505;
    --sidebar: #1e1e1e;
    --nav-text: #a9a9a9;
    --paper: #ffffff;
    --cream: #f4f1e6;
  }
  * { margin: 0; padding: 0; box-sizing: border-box; }
  html, body { width: 1200px; height: 1200px; overflow: hidden; background: var(--paper); }
  body { position: relative; font-family: "Roboto", Arial, sans-serif; }

  /* Website context */
  .site { position: absolute; left: 0; top: 0; width: 1200px; height: 605px; background: var(--sidebar); }
  .sidebar { position: absolute; left: 0; top: 0; width: 202px; height: 573px; background: var(--sidebar); }
  .brand { position: absolute; left: 0; top: 36px; width: 189px; text-align: center; }
  .brand__mark { display: block; width: 40px; height: 40px; margin: 0 auto 10px; background: var(--gold-deep); }
  .brand__name { font-family: "Raleway", sans-serif; font-weight: 400; font-size: 10px; letter-spacing: 3.5px; color: var(--gold-deep); }
  .nav { position: absolute; left: 34px; top: 168px; list-style: none; }
  .nav li { font-family: "Raleway", sans-serif; font-weight: 400; font-size: 12px; color: var(--nav-text); height: 35px; line-height: 16px; }
  .legal { position: absolute; left: 34px; top: 577px; font-family: "Raleway", sans-serif; font-size: 8px; color: #8a8a8a; }

  .hero { position: absolute; left: 202px; top: 0; width: 998px; height: 573px;
    background: linear-gradient(180deg, #4b4f55 0%, #6c6f74 22%, #575752 40%, #6f6c66 60%, #77746f 100%); }
  .hero__title { position: absolute; left: 0; width: 960px; top: 245px; text-align: center;
    font-family: "Raleway", sans-serif; font-weight: 200; font-size: 46px; color: rgba(255,255,255,.55); letter-spacing: 0.5px; }
  .hero__tagline { position: absolute; left: 0; width: 960px; top: 296px; text-align: center;
    font-family: "Playfair Display", serif; font-style: italic; font-weight: 700; font-size: 31px; color: rgba(40,40,40,.7); }
  .hero__cta { position: absolute; left: 0; width: 998px; top: 550px; text-align: center;
    font-family: "Raleway", sans-serif; font-size: 10px; letter-spacing: 2.6px; color: rgba(40,40,40,.8); }

  .cookie { position: absolute; left: 202px; top: 573px; width: 998px; height: 32px; background: var(--sidebar); }
  .cookie__text { position: absolute; left: 210px; top: 10px; font-family: "Raleway", sans-serif; font-size: 9.5px; color: #d6d6d6; }
  .cookie__ok { position: absolute; left: 550px; top: 6px; width: 36px; height: 21px; background: #141414;
    font-family: "Raleway", sans-serif; font-weight: 400; font-size: 9px; color: #fff; text-align: center; line-height: 21px; }

  /* Popup component */
  .popup { position: absolute; width: 343px; height: 342px; background: var(--ink);
    box-shadow: 0 3px 9px rgba(0,0,0,.45); color: var(--cream); text-align: center; }
  .popup--hero { left: 895px; top: 337px; transform: scale(.6); transform-origin: 0 0; box-shadow: 0 0 0 6px rgba(0,0,0,.5); }
  .popup--a { left: 47px; top: 742px; }
  .popup--b { left: 417px; top: 742px; }
  .popup--c { left: 786px; top: 742px; }
  .popup__frame { position: absolute; inset: 9px; border: 2.5px solid var(--gold); }
  .popup__title { position: absolute; left: 0; right: 0; top: 47px; font-size: 36px; line-height: 40px; color: var(--gold); }
  .popup__rule { position: absolute; left: 98px; width: 147px; top: 99px; height: 1.5px; background: var(--gold); }
  .popup__lead { position: absolute; left: 0; right: 0; top: 131px; font-size: 21px; line-height: 24px; }
  .popup__hours { position: absolute; left: 57px; top: 165px; text-align: left; font-size: 21px; line-height: 23px; white-space: pre; }
  .popup__hours .day { color: var(--gold); }
  .popup__button { position: absolute; left: 65px; width: 214px; top: 244px; height: 31px; border-radius: 16px;
    background: var(--gold); color: #1a1a1a; font-size: 15px; line-height: 31px; }
  .popup__link { position: absolute; left: 0; right: 0; top: 283px; font-size: 15px; line-height: 18px; }
  .popup__close { position: absolute; width: 38px; height: 38px; border-radius: 50%; background: var(--ink);
    border: 3px solid var(--gold); box-shadow: 0 2px 5px rgba(0,0,0,.45); }
  .popup__close svg { position: absolute; left: 9px; top: 9px; }
  .popup--a .popup__close { left: 315px; top: -11px; }
  .popup--b .popup__close { left: 150px; top: -20px; }
  .popup--c .popup__close, .popup--hero .popup__close { left: 349px; top: 0; }
</style>
</head>
<body>
  <section class="site">
    <aside class="sidebar">
      <div class="brand"><span class="brand__mark"></span><span class="brand__name">WANDELHOF</span></div>
      <ul class="nav">
        <li>ÜBER UNS</li><li>KAMINÖFEN</li><li>HOLZKAMINE</li><li>GASKAMINE</li><li>AUSSTELLUNG</li><li>KONTAKT</li>
      </ul>
      <p class="legal">Impressum | Datenschutz</p>
    </aside>
    <div class="hero" role="img" aria-label="Foto: hängender schwarzer Designkamin vor Panoramafenster mit Berglandschaft">
      <h1 class="hero__title">WILLKOMMEN IM WANDELHOF</h1>
      <p class="hero__tagline">KAMINE FÜRS LEBEN</p>
      <p class="hero__cta">Jetzt Beratungstermin vereinbaren</p>
    </div>
    <div class="cookie">
      <p class="cookie__text">Wir nutzen Cookies, um Ihnen auch online den besten Service zu bieten.</p>
      <span class="cookie__ok">Ok.</span>
    </div>
  </section>

  <div class="popup popup--hero">
    <div class="popup__frame"></div>
    <h2 class="popup__title">Öffnungszeiten</h2><div class="popup__rule"></div>
    <p class="popup__lead">Wir haben für Sie geöffnet:</p>
    <p class="popup__hours"><span class="day">Fr  17.01.</span> 14:00 - 17:00 Uhr
<span class="day">Sa 18.01.</span> 10:00 - 13:00 Uhr</p>
    <div class="popup__button">Weitere Termine ansehen</div>
    <p class="popup__link">Individuellen Termin vereinbaren</p>
    <div class="popup__close"><svg width="14" height="14" viewBox="0 0 14 14"><path d="M1 1L13 13M13 1L1 13" stroke="#f4f1e6" stroke-width="2.6"/></svg></div>
  </div>

  <div class="popup popup--a">
    <div class="popup__frame"></div>
    <h2 class="popup__title">Öffnungszeiten</h2><div class="popup__rule"></div>
    <p class="popup__lead">Wir haben für Sie geöffnet:</p>
    <p class="popup__hours"><span class="day">Fr  17.01.</span> 14:00 - 17:00 Uhr
<span class="day">Sa 18.01.</span> 10:00 - 13:00 Uhr</p>
    <div class="popup__button">Weitere Termine ansehen</div>
    <p class="popup__link">Individuellen Termin vereinbaren</p>
    <div class="popup__close"><svg width="14" height="14" viewBox="0 0 14 14"><path d="M1 1L13 13M13 1L1 13" stroke="#f4f1e6" stroke-width="2.6"/></svg></div>
  </div>

  <div class="popup popup--b">
    <div class="popup__frame"></div>
    <h2 class="popup__title">Öffnungszeiten</h2><div class="popup__rule"></div>
    <p class="popup__lead">Wir haben für Sie geöffnet:</p>
    <p class="popup__hours"><span class="day">Fr  17.01.</span> 14:00 - 17:00 Uhr
<span class="day">Sa 18.01.</span> 10:00 - 13:00 Uhr</p>
    <div class="popup__button">Weitere Termine ansehen</div>
    <p class="popup__link">Individuellen Termin vereinbaren</p>
    <div class="popup__close"><svg width="14" height="14" viewBox="0 0 14 14"><path d="M1 1L13 13M13 1L1 13" stroke="#f4f1e6" stroke-width="2.6"/></svg></div>
  </div>

  <div class="popup popup--c">
    <div class="popup__frame"></div>
    <h2 class="popup__title">Öffnungszeiten</h2><div class="popup__rule"></div>
    <p class="popup__lead">Wir haben für Sie geöffnet:</p>
    <p class="popup__hours"><span class="day">Fr  17.01.</span> 14:00 - 17:00 Uhr
<span class="day">Sa 18.01.</span> 10:00 - 13:00 Uhr</p>
    <div class="popup__button">Weitere Termine ansehen</div>
    <p class="popup__link">Individuellen Termin vereinbaren</p>
    <div class="popup__close"><svg width="14" height="14" viewBox="0 0 14 14"><path d="M1 1L13 13M13 1L1 13" stroke="#f4f1e6" stroke-width="2.6"/></svg></div>
  </div>
</body>
</html>
```